HIGH END MEDICAL/ANTI-AGING START-UP BROCHURE + BUSINESS CARDS

Fernridgewellnessco.example needs a brochure which details our two top selling products. The Vital Matrix Profile Review (VMP) coupled with the 4(16) Plan.

Here is some information about the VMP and the 4(16) plan. Please see our website for pictures and color.

VMP-Vital Matrix Profile and Fernridge
Fernridge Wellness Co is changing the way people look at health by bringing the focus back to the physical examination and patient centered care. It's our new, cutting edge system, Vital Matrix Profile, that allows us to have unparalleled patient outcomes. Vital Matrix Profile is a true deep dive into the individual. The protocol assesses, measures and tracking over 70 different bio-parameters such as hormone balance, tissue health, muscle mass, fat mass, frame mass, water content, water distribution, and acid/alkaline balance. This new analytics tool allows hyper individualized and customized weight loss and health programs to evolve in a new and never before seen way.

The 4(16) Plan
The 4(16) Cleanse plan works by creating a full metabolic reset geared towards facilitation of hormone optimization and balance as well as toxicity and fat removal. Toxins are fat soluble and often need targeted nutritional strategy for long-term weight loss to occur; this is why many people do not lose weight even on calorie restricted diets with exercise plans until they use proper nutritional protocol. The 4(16) Cleanse allows for fat cells to be released and disposed of while at the same time adding deficient nutrients back into the tissues, helping you to not only lose weight, but reach optimal health and hormonal balance at the same time.

Target Market(s)

High-end and upscale clients looking for boutique medical services. We deal with clients mostly in executive level finance.

Industry/Entity Type

Medical

Contact Information for Business Card

-Must have our logo
-website (fernridgewellnessco.example)
-a space for our titles, "Dr. Anton Pelsing, Founder" & "Rosalind Pelsing, Program Director"
-office phone number and our cell phone numbers (we will give you our cell phone numbers later)

Font styles to use
Serif
Sans Serif

Colors
0355a3
0493ce
00a990
ffffff
000000
919191
474747

Requirements
Must have
• Brochure and business cards must be VERY modern, creative and sophisticated.
Nice to have
• Usage of the company colors and logo in a new and interesting way.
Should not have
• Do not use colors outside of our logo + black + grey or white.
• Nothing cartoonish.

```html
<!DOCTYPE html>
<html lang="en">
<head>
<meta charset="utf-8">
<title>Fernridge Wellness Co — Trifold Brochure</title>
<link href="https://fonts.googleapis.com/css2?family=Montserrat:wght@400;600;700&family=Open+Sans:wght@400;600;700&display=swap" rel="stylesheet">
<style>
:root{
  --green:#1f9d4a;
  --green-dark:#178a3e;
  --blue:#3b6fd6;
  --blue-deep:#2a56b8;
  --ink:#474747;
  --grey:#919191;
  --paper:#ffffff;
  --stage:#e6e6e6;
}
*{box-sizing:border-box;margin:0;padding:0}
html,body{width:848px;height:1200px;overflow:hidden;background:var(--stage);font-family:"Open Sans",Arial,sans-serif;color:var(--ink)}
.spread{position:absolute;left:24px;width:800px;height:520px;display:flex;background:var(--paper);box-shadow:0 6px 18px rgba(0,0,0,.18)}
.spread--outside{top:46px}
.spread--inside{top:634px}
.panel{position:relative;width:266.67px;height:520px;overflow:hidden}
.panel + .panel{border-left:1px solid rgba(0,0,0,.06)}
.bg{position:absolute;inset:0;width:100%;height:100%}
.photo{position:absolute;border-radius:50%;border:4px solid var(--paper)}
.pill{position:absolute;font-family:"Montserrat",Arial,sans-serif;font-weight:700;font-size:7.5px;letter-spacing:.3px;padding:3px 9px;border-radius:10px;white-space:nowrap}
.pill--white{background:var(--paper);color:var(--green)}
.pill--green{background:var(--green);color:var(--paper)}
.pill--boxed{background:var(--paper);color:var(--blue-deep);border-radius:2px;font-size:9px}
.copy{position:absolute;font-size:6.6px;line-height:1.45}
.copy--light{color:var(--paper)}
.copy--center{text-align:center}
.brand-top{position:absolute;top:14px;right:16px;font-family:"Montserrat",Arial,sans-serif;font-weight:700;font-size:7.5px;color:var(--paper);letter-spacing:.4px}
.contact{position:absolute;left:34px;top:268px;font-size:8px;color:var(--ink)}
.contact h4{font-family:"Montserrat",Arial,sans-serif;font-size:9.5px;color:var(--green);text-decoration:underline;margin-top:6px;letter-spacing:.3px}
.contact p{display:flex;gap:5px;align-items:flex-start;line-height:1.35;font-weight:600}
.contact svg{flex:none;margin-top:1px}
.social{display:flex;gap:8px;margin-top:6px}
.social span{width:17px;height:17px;border-radius:50%;background:var(--blue)}
.logo{position:absolute;left:82px;top:318px;display:flex;align-items:center;gap:6px}
.logo .mark{width:26px;height:26px;border-radius:50%;background:var(--green)}
.logo .name{font-family:"Montserrat",Arial,sans-serif;font-weight:700;font-size:11px;color:var(--blue-deep);line-height:1.1}
.tagline{position:absolute;left:28px;top:388px;font-family:"Montserrat",Arial,sans-serif;color:var(--ink);line-height:1}
.tagline .t1{font-size:21px;font-weight:400}
.tagline .t2{font-size:32px;font-weight:700;color:var(--green);margin:2px 0}
.tagline .t3{font-size:21px;font-weight:400}
.sub{position:absolute;font-size:7.4px;font-weight:700;text-decoration:underline;display:flex;gap:4px;align-items:center}
.sub--blue{color:var(--blue-deep)}
.sub--light{color:var(--paper)}
.sub i{width:0;height:0;border-left:5px solid currentColor;border-top:3.5px solid transparent;border-bottom:3.5px solid transparent}
</style>
</head>
<body>

<!-- OUTSIDE -->
<section class="spread spread--outside">
  <!-- back flap -->
  <div class="panel panel--flap">
    <svg class="bg" viewBox="0 0 267 520" preserveAspectRatio="none">
      <rect width="267" height="520" fill="#1f9d4a"/>
      <path d="M0 245 Q150 215 267 270 L267 520 L0 520Z" fill="#ffffff"/>
      <path d="M0 256 Q150 228 267 282 L267 520 L0 520Z" fill="#3b6fd6"/>
    </svg>
    <div class="brand-top">FERNRIDGE WELLNESS CO</div>
    <div class="photo" role="img" aria-label="Photo of a body contour close-up" style="left:96px;top:34px;width:76px;height:76px;background:radial-gradient(circle at 50% 45%,#e8c9b3,#c59b83)"></div>
    <div class="pill pill--white" style="left:70px;top:116px">VMP-VITAL MATRIX PROFILE</div>
    <p class="copy copy--light copy--center" style="left:20px;top:136px;width:228px">Fernridge Wellness Co is changing the way people look at health by bringing the focus back to the physical examination and patient centered care. Our new, cutting edge system, Vital Matrix Profile, allows unparalleled patient outcomes. It is a true deep dive into the individual, tracking over 70 different bio-parameters such as hormone balance, tissue health, muscle mass, fat mass, water content and acid/alkaline balance. This tool allows hyper individualized weight loss and health programs to evolve in a new and never before seen way.</p>
    <div class="photo" role="img" aria-label="Photo of a woman holding fresh vegetables" style="left:40px;top:258px;width:72px;height:72px;background:radial-gradient(circle at 50% 40%,#d9b49a,#5a8a3a)"></div>
    <div class="pill pill--white" style="left:106px;top:336px;color:var(--blue-deep)">THE 4(16) PLAN</div>
    <p class="copy copy--light copy--center" style="left:20px;top:356px;width:228px">The 4(16) Cleanse plan works by creating a full metabolic reset geared towards hormone optimization and balance as well as toxicity and fat removal. Toxins are fat soluble and often need a targeted nutritional strategy for long-term weight loss; this is why many people do not lose weight even on restricted diets until they use proper nutritional protocol. The 4(16) Cleanse allows fat cells to be released while adding deficient nutrients back into the tissues, helping you reach optimal health and hormonal balance at the same time.</p>
  </div>

  <!-- contact panel -->
  <div class="panel panel--contact">
    <div class="bg" role="img" aria-label="Faint snowy mountain landscape" style="background:linear-gradient(180deg,#c9d7e6 0%,#e9eef3 35%,#f6f7f8 70%,#eef2f5 100%)"></div>
    <div class="contact">
      <h4>ADDRESS</h4>
      <p><svg width="7" height="9" viewBox="0 0 7 9"><path d="M3.5 0A3.2 3.2 0 0 0 .3 3.2C.3 5.6 3.5 9 3.5 9S6.7 5.6 6.7 3.2A3.2 3.2 0 0 0 3.5 0Zm0 4.4a1.2 1.2 0 1 1 0-2.4 1.2 1.2 0 0 1 0 2.4Z" fill="#1f9d4a"/></svg><span>Fernridge Wellness Co<br>18 Lantern Way Suite 120<br>Harbor Falls CT, 06011</span></p>
      <p style="margin-top:3px"><svg width="7" height="9" viewBox="0 0 7 9"><path d="M3.5 0A3.2 3.2 0 0 0 .3 3.2C.3 5.6 3.5 9 3.5 9S6.7 5.6 6.7 3.2A3.2 3.2 0 0 0 3.5 0Zm0 4.4a1.2 1.2 0 1 1 0-2.4 1.2 1.2 0 0 1 0 2.4Z" fill="#1f9d4a"/></svg><span>New York Office:<br>240 Mercer Row<br>Eastbrook, NY, 10099</span></p>
      <h4>TELEPHONE</h4>
      <p><svg width="8" height="8" viewBox="0 0 8 8"><path d="M1.6.3 2.8 2 2.1 3a4.6 4.6 0 0 0 2.9 2.9l1-.7 1.7 1.2-.6 1.3C3.4 7.5.5 4.6.3 1Z" fill="#1f9d4a"/></svg><span>(555) 014-2730</span></p>
      <h4>EMAIL</h4>
      <p><svg width="8" height="7" viewBox="0 0 8 7"><rect x=".3" y=".8" width="7.4" height="5.4" fill="none" stroke="#1f9d4a"/><path d="M.3 .8 4 4 7.7 .8" fill="none" stroke="#1f9d4a"/></svg><span>info@Fernridgewellnessco.example</span></p>
      <h4>FOLLOW US AT</h4>
      <div class="social"><span></span><span></span></div>
    </div>
  </div>

  <!-- cover -->
  <div class="panel panel--cover">
    <svg class="bg" viewBox="0 0 267 520" preserveAspectRatio="none">
      <rect width="267" height="520" fill="#f4f5f6"/>
      <path d="M40 0 L267 0 L267 330 Q150 350 90 260 Q30 150 40 0Z" fill="#1f9d4a"/>
      <circle cx="190" cy="165" r="118" fill="#3b6fd6"/>
      <circle cx="186" cy="165" r="112" fill="#ffffff"/>
    </svg>
    <div class="photo" role="img" aria-label="Photo of a woman with open arms among green trees" style="left:86px;top:64px;width:196px;height:196px;border:0;background:radial-gradient(circle at 55% 55%,#e8ecdf 0%,#9bc35a 35%,#4f8a2a 80%)"></div>
    <div class="logo"><span class="mark"></span><span class="name">FERNRIDGE<br>WELLNESS CO</span></div>
    <div class="tagline">
      <div class="t1">When your body</div>
      <div class="t2">FEELS GOOD</div>
      <div class="t3">life feels good</div>
    </div>
  </div>
</section>

<!-- INSIDE -->
<section class="spread spread--inside">
  <!-- VMP panel -->
  <div class="panel">
    <svg class="bg" viewBox="0 0 267 520" preserveAspectRatio="none">
      <rect width="267" height="520" fill="#ffffff"/>
      <path d="M0 0 H267 V100 Q200 160 60 150 Q20 148 0 140Z" fill="#3b6fd6"/>
      <path d="M0 0 H267 V92 Q200 148 60 140 Q20 138 0 130Z" fill="#1f9d4a"/>
      <path d="M0 0 H258 V84 Q195 135 60 128 Q20 126 0 118Z" fill="#ffffff"/>
    </svg>
    <div class="bg" role="img" aria-label="Photo of a body contouring treatment" style="clip-path:path('M0 0 H254 V80 Q192 128 60 122 Q20 120 0 112Z');background:linear-gradient(120deg,#f2f2f2 0%,#e2bca2 45%,#c8906f 75%,#efe6df 100%)"></div>
    <div class="pill pill--green" style="left:30px;top:168px">VMP-VITAL MATRIX PROFILE</div>
    <div class="sub sub--blue" style="left:22px;top:194px"><i></i>LEANNESS &amp; HEALTH</div>
    <p class="copy" style="left:22px;top:207px;width:226px">The scientific community has held lean body composition as one of the key tenets in maintaining good health for decades. Yet, we are the fattest nation in the world and the weight loss industry keeps booming and failing all in the same. Lifestyle diseases are taking over our healthcare system with no definitive forms of treatment, while at the same time, expensive drugs are failing our families and communities. Why? The answer is a lack of an effective way to assess, track and treat body composition. The better your body composition and cellular health is, the better you feel and look, and the better you can be a role model for those you care about. Whatever your reason for changing your body composition, weight loss, health or vanity, we're on board!</p>
    <div class="sub sub--blue" style="left:22px;top:340px"><i></i>BEING LEAN FOR HEALTH AND VANITY = 'S HEALTHY VANITY!</div>
    <p class="copy" style="left:22px;top:353px;width:226px">Dr. Anton has coined the term "healthy vanity" to popularize the realization that looking and feeling good are often one in the same, and that we shouldn't feel guilty for making and wanting our insides and our outsides to be healthy as well as aesthetically pleasing.</p>
    <div role="img" aria-label="Black and white mountain range" style="position:absolute;left:0;bottom:0;width:267px;height:95px;background:linear-gradient(180deg,#ffffff 0%,#cfcfcf 35%,#6c6c6c 70%,#3a3a3a 100%)"></div>
  </div>

  <!-- 4(16) panel -->
  <div class="panel" style="background:var(--blue)">
    <div role="img" aria-label="Photo of fresh carrots, kale and vegetables" style="position:absolute;left:0;top:0;width:267px;height:92px;clip-path:path('M0 0 H267 V70 Q150 92 0 80Z');background:linear-gradient(90deg,#e07a2a 0%,#4f8a2a 40%,#2f6a28 65%,#c93a2a 80%,#9ac25a 100%)"></div>
    <div class="pill pill--boxed" style="left:22px;top:100px">THE 4(16) PLAN</div>
    <div class="sub sub--light" style="left:22px;top:124px"><i></i>THE 4(16) CLEANSE</div>
    <p class="copy copy--light" style="left:22px;top:137px;width:226px">The 4(16) Cleanse is an intensive cleansing week followed by a 16-day maintenance program. All 4(16) plans are completely customized. Customization of patient programming is dependent upon results reported following the Vital Matrix Profile review. Following the intensive 4-day period, Fernridge Wellness Co guides clients into the 16-day maintenance portion of the program. Specific diet and lifestyle counseling is given for these weeks to ensure the continued success of the patient.</p>
    <div class="sub sub--light" style="left:22px;top:236px"><i></i>WHY WE CHOSE DETOX AS OUR PRIMARY METHOD OF TREATMENT</div>
    <p class="copy copy--light" style="left:22px;top:260px;width:226px">There are over 80,000 registered chemicals in the atmosphere, and science over the past 20 years has identified a huge number of specific toxic compounds, ubiquitous to the environment, that fall into the category of endocrine disruptors or excitotoxins. These terms refer to toxins which either affect the brain, or the way your body produces and uses hormones. Once we are able to rid the body of toxicity, many ailments resolve themselves without pharmacological treatment or disease progression.</p>
    <div role="img" aria-label="Blue-toned snowy mountain peaks" style="position:absolute;left:0;bottom:0;width:267px;height:130px;background:linear-gradient(180deg,rgba(59,111,214,0) 0%,#6f95dd 35%,#dfe8f6 60%,#3152a8 100%)"></div>
  </div>

  <!-- detox panel -->
  <div class="panel">
    <p class="copy" style="left:22px;top:22px;width:226px">There are over 80,000 registered chemicals in the atmosphere, and for the most part, the information and science is lacking in regards to how they affect the human body, as well as our environment. Toxins have been linked to almost every disease imaginable on some level or mechanism. Toxins are direct mitochondrial poisons, meaning they drastically affect how your body produces the energy it needs to live and thrive.</p>
    <div class="sub sub--blue" style="left:22px;top:108px"><i></i>WHY WE CHOSE DETOX AS OUR PRIMARY METHOD OF TREATMENT</div>
    <p class="copy" style="left:22px;top:132px;width:226px">An interesting study was published in the 90's and it talked about the signs and symptoms of chronic poisoning. The signs of chronic poisoning were found to be the same seen everyday in medical offices and homes around the country: fatigue, headaches, inability to lose weight and many more. Fernridge Wellness Co uses detoxification as a baseline for treatment. Conventional medicine looks to add and add substances and drugs into the body in order to elicit change. We take a different approach, utilizing the latest in detoxification and biotransformation techniques to help pull toxic substances out of the body. When toxins are eliminated, energy systems work more efficiently and create a happier and healthier environment in the body.</p>
    <svg style="position:absolute;left:0;top:0" width="267" height="520" viewBox="0 0 267 520">
      <path d="M0 300 Q140 250 267 275 V520 H0Z" fill="#3b6fd6"/>
      <path d="M0 308 Q140 260 267 284 V520 H0Z" fill="#1f9d4a"/>
      <path d="M0 318 Q140 272 267 296 V520 H0Z" fill="#ffffff"/>
    </svg>
    <div role="img" aria-label="Photo of a slim waist with a measuring tape" style="position:absolute;left:0;top:0;width:267px;height:520px;clip-path:path('M0 324 Q140 280 267 304 V520 H0Z');background:linear-gradient(90deg,#b9d8e6 0%,#e7c3a8 35%,#d8a887 55%,#f3f3f3 75%,#a9d0e3 100%)"></div>
  </div>
</section>

</body>
</html>
```